Classy, Elegant, Simple Business Card Design

Looking to have a classy, simple, and elegant design. Want a top notch designed business card. I really like the look of the new brivo credit card. I also like the design I attached. I am trying to reach 21-29 year old females for booking us for there wedding or event. We offer Disc Jockey Service, Photo Booth Rentals, and Uplighting .

Target Market(s)

21-28 year old females

Contact Information for Business Card

Has to have logo, website, email, and phone number

Font styles to use
Other font styles liked:
• open to font choice, modern, clean
Designer to choose
33a6d7
0791cd
0555a3
ffffff

Requirements
Must have
• Has to have logo, website, email, and phone number
Nice to have
• I really like the design of the new brivo credit card. I also included my logo and some designs I like
Should not have
• clutter or too much info

```html
<!DOCTYPE html>
<html lang="en">
<head>
<meta charset="utf-8">
<title>Tidewell Event Group – Business Card</title>
<link rel="stylesheet" href="https://fonts.googleapis.com/css2?family=Poppins:wght@400;500&display=swap">
<style>
  :root {
    --stage: #1c1c1c;
    --paper: #ffffff;
    --brand-light: #33a6d7;
    --brand-mid: #0791cd;
    --brand-deep: #0555a3;
    --ink: #3a3a3a;
    --muted: #9a9a9a;
  }
  * { margin: 0; padding: 0; box-sizing: border-box; }
  html, body { width: 1200px; height: 1200px; overflow: hidden; }
  body {
    background: var(--stage);
    font-family: "Poppins", sans-serif;
    position: relative;
  }
  .card {
    position: absolute;
    left: 262px;
    width: 686px;
    height: 392px;
  }
  .card-front { top: 165px; background: var(--paper); }
  .card-back {
    top: 653px;
    background: radial-gradient(ellipse at 55% 45%, #0aa6e4 0%, #128fd6 55%, #1a7cc6 100%);
  }
  .brand-lockup {
    position: absolute;
    right: 70px;
    top: 110px;
    display: flex;
    align-items: center;
    gap: 12px;
  }
  .brand-dot {
    width: 14px; height: 14px;
    border-radius: 50%;
    background: var(--brand-deep);
  }
  .brand-name {
    font-size: 26px;
    font-weight: 500;
    color: var(--brand-deep);
    letter-spacing: 0.5px;
  }
  .person {
    position: absolute;
    left: 39px;
    top: 298px;
    font-size: 24px;
    font-weight: 500;
    color: var(--brand-mid);
  }
  .person .role {
    font-size: 16px;
    font-weight: 400;
    color: var(--muted);
  }
  .contact {
    position: absolute;
    left: 39px;
    top: 336px;
    font-size: 16px;
    color: var(--ink);
    white-space: nowrap;
  }
  .contact .label { color: var(--brand-mid); }
  .back-name {
    position: absolute;
    left: 0; right: 0;
    top: 160px;
    text-align: center;
    font-size: 50px;
    font-weight: 500;
    color: var(--paper);
    letter-spacing: 1px;
  }
  .services {
    position: absolute;
    left: 0; right: 0;
    top: 336px;
    text-align: center;
    font-size: 16px;
    font-weight: 500;
    color: var(--paper);
  }
</style>
</head>
<body>
  <section class="card card-front">
    <div class="brand-lockup">
      <span class="brand-dot"></span>
      <span class="brand-name">Tidewell Event Group</span>
    </div>
    <p class="person">Daniel Porter- <span class="role">President</span></p>
    <p class="contact">
      <span class="label">P.</span> 555-014-2738
      <span class="label">E.</span> hello@tidewellevents.com
      <span class="label">W.</span> tidewellevents.com
    </p>
  </section>

  <section class="card card-back">
    <p class="back-name">Tidewell</p>
    <p class="services">Disc Jockey Service • Photo Booth Rentals • Uplighting .</p>
  </section>
</body>
</html>
```